Venture Capital firm needs modern business cards

We are a Venture Capital firm within financial services/Asset management. The industry generally has basic business cards with black, blue and maybe green/yellow design elements.
Our firm has a four-colour swoosh logo. We are based in London and want to stand out, just a little bit!, from the crowd. Our company is called MOBRA Holdings and the 'C' stands for collaboration thus using pixelfair is a natural portal for our business card design competition. Our logo came via pixelfair too!
We use 'Venture Partner in Asset Management' as our tagline and this is Trademark registered. We operate in a conservative industry and we should not overstep our mark. The logo is colorful as it is and therefore the rest of the design should not be too fanciful.
The objective is twofold: make our logo element stick and memorable with our audience, whilst representing a conservative yet young image.
Updates
The Business Card obviously needs a field for Name, Surname, Job Title, Adress fields: Street, City, Postcode, Country, telefone and cell number, website address, etc.
We have uploaded the ai file. We trust that these are OK. If not, please advise.
Reason: We have have been busy with a client engagement. We will set the project as Guaranteed in return for the troubles we cause. Apologies for the confusion.
Thank you all for these great and creative design suggestions. The team is very happy with a number of your ideas! We will be in touch tomorrow to give individual feedback before the project closes on Friday. We look forward to working with some of you to narrow down your creations. Thank you, MOBRA Holdings team.
All,
Target Market(s)
Financial Services Professionals, Investors, Media, 35-70 years, mainly male, well educated
Industry/Entity Type
Conservative
Requirements
Must have
- We must make use of our logo and potential tagline 'Venture Partner in Asset Management' as we are establishing a new Brand and new company in the market.
We can use 'MOBRA', 'MOBRA Holdings', and 'MOBRA Holdings'+tagline 'Venture Partner in Asset Management' or simply the four-colour swoosh plus the name of the company as part of the text. (see files)
All design elements are available in black or grey-scale if required. (grey scale swoosh attached).
Due to regulation we must have the following wording on the card in small print 'MOBRA Holdings is an Appointed Representative of Warbeck Ledger Advisory Limited, which is authorised by the Monetary Standards Bureau'.
Nice to have
- We would consider designs that make use of different printing techniques such embossing/debossing, UV spot etc.
We attach our colour palette in the files section for your reference.
Should not have
- The font we use for our company name is 'EXO' so do not use a font style that clashes with the corporate fonts, please.
Do not use other design elements than the ones we provide in the file library as part of this project.

```html
<!DOCTYPE html>
<html lang="en">
<head>
<meta charset="utf-8">
<title>MOBRA Holdings – Business Card</title>
<link rel="stylesheet" href="https://fonts.googleapis.com/css2?family=Exo:wght@500;600&family=Open+Sans:wght@400;600;700&display=swap">
<style>
  :root {
    --page: #e9e7e4;
    --card-dark: #2a2a2c;
    --card-dark-edge: #1c1c1e;
    --card-light: #ffffff;
    --ink-dark: #3a3a3c;
    --ink-grey: #8a8a8c;
    --accent-teal: #29a9c9;
    --white: #ffffff;
  }
  * { box-sizing: border-box; margin: 0; padding: 0; }
  html, body { width: 1200px; height: 900px; overflow: hidden; }
  body {
    background: var(--page);
    position: relative;
    font-family: "Open Sans", Arial, sans-serif;
  }
  .card {
    position: absolute;
    width: 640px;
    height: 366px;
    overflow: hidden;
    box-shadow: 0 10px 28px rgba(0,0,0,.22);
  }

  /* Front: dark side */
  .card--front {
    left: 110px; top: 60px;
    background: linear-gradient(135deg, #3a3a3d 0%, var(--card-dark) 45%, var(--card-dark-edge) 100%);
    color: var(--white);
  }
  .front-brand {
    position: absolute;
    right: 40px; top: 36px;
    text-align: right;
  }
  .front-brand .wordmark {
    font-family: "Exo", Arial, sans-serif;
    font-weight: 600;
    font-size: 82px;
    line-height: 1;
    letter-spacing: 1px;
    color: var(--white);
  }
  .front-brand .tagline {
    font-weight: 700;
    font-size: 12px;
    margin-top: 8px;
    color: var(--white);
  }
  .regulatory {
    position: absolute;
    right: 36px; bottom: 34px;
    width: 560px;
    text-align: right;
    font-size: 13.5px;
    line-height: 1.35;
    color: var(--white);
  }

  /* Back: white side */
  .card--back {
    left: 450px; top: 478px;
    background: var(--card-light);
  }
  .back-panel {
    position: absolute;
    inset: 0;
    width: 640px; height: 366px;
  }
  .back-brand {
    position: absolute;
    left: 38px; top: 40px;
  }
  .back-brand .mark-row {
    display: flex;
    align-items: center;
    gap: 12px;
  }
  .back-brand .brand-dot {
    width: 30px; height: 30px;
    border-radius: 50%;
    background: var(--accent-teal);
  }
  .back-brand .wordmark {
    font-family: "Exo", Arial, sans-serif;
    font-weight: 600;
    font-size: 50px;
    line-height: 1;
    color: var(--ink-dark);
  }
  .back-brand .tagline {
    font-weight: 700;
    font-size: 9px;
    color: var(--ink-dark);
    margin: 4px 0 0 42px;
  }
  .address {
    position: absolute;
    left: 40px; top: 160px;
    font-size: 16px;
    font-style: normal;
    line-height: 1.35;
    color: var(--ink-grey);
  }
  .contacts {
    position: absolute;
    left: 40px; top: 222px;
    list-style: none;
    font-size: 16px;
    line-height: 1.45;
    color: var(--ink-grey);
  }
  .contacts li { display: flex; align-items: center; gap: 9px; }
  .contacts svg { width: 13px; height: 13px; fill: var(--accent-teal); flex: none; }
  .person {
    position: absolute;
    right: 36px; top: 188px;
    text-align: right;
    width: 200px;
  }
  .person .name {
    font-family: "Exo", Arial, sans-serif;
    font-weight: 600;
    font-size: 21px;
    color: var(--accent-teal);
  }
  .person .role {
    font-size: 15px;
    color: var(--white);
    margin-top: 2px;
  }
</style>
</head>
<body>

  <section class="card card--front" aria-label="Business card front">
    <div class="front-brand">
      <div class="wordmark">MOBRA</div>
      <div class="tagline">Venture Partner in Asset Management</div>
    </div>
    <p class="regulatory">MOBRA Holdings is an Appointed Representative of Warbeck Ledger Advisory Limited, which is authorised by the Monetary Standards Bureau</p>
  </section>

  <section class="card card--back" aria-label="Business card back">
    <svg class="back-panel" viewBox="0 0 640 366" aria-hidden="true">
      <path d="M420 0 H640 V366 H420 Q360 183 420 0 Z" fill="#2a2a2c"/>
      <path d="M404 0 Q344 183 404 366" fill="none" stroke="#29a9c9" stroke-width="3"/>
    </svg>

    <div class="back-brand">
      <div class="mark-row">
        <span class="brand-dot"></span>
        <span class="wordmark">MOBRA</span>
      </div>
      <div class="tagline">Venture Partner in Asset Management</div>
    </div>

    <address class="address">
      418 Fenwick Lane, Suite 12<br>
      Box 305 Harlow, CM19 4QT
    </address>

    <ul class="contacts">
      <li>
        <svg viewBox="0 0 16 16"><path d="M3 1h3l1.5 4-2 1.3a8 8 0 0 0 4.2 4.2L11 8.5l4 1.5v3a2 2 0 0 1-2 2A12 12 0 0 1 1 3a2 2 0 0 1 2-2z"/></svg>
        020-555-0187
      </li>
      <li>
        <svg viewBox="0 0 16 16"><rect x="1" y="11" width="3" height="4"/><rect x="5" y="8" width="3" height="7"/><rect x="9" y="5" width="3" height="10"/><rect x="13" y="1" width="3" height="14"/></svg>
        077-555-0142
      </li>
      <li>
        <svg viewBox="0 0 16 16"><path d="M1 3h14v10H1z M2.5 4.5 8 9l5.5-4.5v-.2H2.5z" fill-rule="evenodd"/></svg>
        info@mobra.com
      </li>
      <li>
        <svg viewBox="0 0 16 16"><circle cx="8" cy="8" r="7"/></svg>
        www.mobra.com
      </li>
    </ul>

    <div class="person">
      <div class="name">Daniel Hartley</div>
      <div class="role">Vice President</div>
    </div>
  </section>

</body>
</html>
```